<作成物>
■リッチメッセージ
リッチメニュー
合計2枚

〈リッチメニューの項目〉
下の段左から右へ①〜③
下の段左から右へ④〜⑤

〈リッチメニューの表示名〉
①ホームページ ②メニュー   ③SNS
④お客様の声  ⑤スタッフ・店 ⑥予約

デザイン重視でここの表示名はデザイン的に英語の方がよければ
英語でも大丈夫です。意味がわかって
ニュアンスがあっていれば文字を短くするのも
お任せします。あくまでデザイン重視です。

〈画像はこちらから〉

画像
https://47.kovaload.zz/0922-ab73c1d0e5f2a4b6c8d9e0f1a2b3c4d5e6

ロゴ
https://61.kovaload.zz/0922-3d91f7a2c4b6e8d0f1a3c5e7b9d2f4a6c8

※こちらの作成以外に勝手に使用された場合は
著作権侵害で法的手段をとらせていただきます。
作成事例にもしようしないでください。

<サイズ>
・リッチメッセージ(1040×1040ピクセル)
・リッチメニュー(1200×810ピクセル)

<納品形式>
・ai形式(イラストレーターデータ)
・JPG
<詳細>
※添付ファイルをご確認ください。

<備考>
ブランディング効果を期待しています。
どんどん何個でも応募ください。

```html
<!DOCTYPE html>
<html lang="ja">
<head>
<meta charset="utf-8">
<title>素肌研究室 リッチメッセージ・リッチメニュー</title>
<link href="https://fonts.googleapis.com/css2?family=Noto+Serif+JP:wght@500;700&family=Noto+Sans+JP:wght@500&family=Patrick+Hand&display=swap" rel="stylesheet">
<style>
  :root{
    --page:#ffffff;
    --frame:#1f2b4d;
    --band-a:#c07d12;
    --band-b:#e6a43a;
    --band-text:#ffffff;
    --photo-skin-a:#f3e6dc;
    --photo-skin-b:#e8cdbb;
    --photo-room-a:#4a3426;
    --photo-room-b:#9a7656;
    --photo-care-a:#c9a58a;
    --photo-care-b:#efe0d2;
    --menu-bg-a:#76b9c6;
    --menu-bg-b:#9fd0d8;
    --tile-gold:#efb33e;
    --tile-lime:#dde0a0;
    --tile-orange:#ec8a3c;
    --ink:#3b3b3b;
    --logo-ink:#4a3a30;
  }
  *{box-sizing:border-box;margin:0;padding:0}
  html,body{width:798px;height:1200px;overflow:hidden;background:var(--page)}
  .canvas{position:relative;width:798px;height:1200px}

  /* Rich message */
  .rich-message{position:absolute;left:93px;top:32px;width:612px;height:612px;border:5px solid var(--frame);overflow:hidden;background:var(--photo-skin-a)}
  .hero-photo{position:absolute;left:0;top:0;width:100%;height:368px;background:linear-gradient(160deg,var(--photo-skin-a) 0%,var(--photo-skin-b) 70%,#d9b8a2 100%)}
  .brand{position:absolute;left:16px;top:12px;display:flex;align-items:center;gap:8px;font-family:"Noto Serif JP",serif;font-weight:700;font-size:26px;color:var(--logo-ink)}
  .brand-mark{width:22px;height:22px;border-radius:50%;background:var(--logo-ink)}
  .tagline{position:absolute;left:0;top:368px;width:100%;height:100px;background:linear-gradient(90deg,var(--band-a),var(--band-b) 50%,var(--band-a));display:flex;flex-direction:column;justify-content:center;align-items:center;font-family:"Noto Serif JP",serif;font-weight:500;font-size:31px;line-height:1.3;color:var(--band-text);letter-spacing:1px}
  .room-photo{position:absolute;left:0;top:468px;width:418px;height:134px;background:linear-gradient(100deg,var(--photo-room-a),var(--photo-room-b) 60%,#c7a987)}
  .care-photo{position:absolute;left:418px;top:468px;width:184px;height:134px;background:linear-gradient(120deg,var(--photo-care-a),var(--photo-care-b))}

  /* Rich menu */
  .rich-menu{position:absolute;left:48px;top:686px;width:702px;height:474px;padding:16px;background:linear-gradient(135deg,var(--menu-bg-a),var(--menu-bg-b) 55%,var(--menu-bg-a));display:grid;grid-template-columns:repeat(3,1fr);grid-template-rows:repeat(2,1fr);gap:14px}
  .menu-tile{position:relative;display:flex;flex-direction:column;align-items:center;padding-top:14px;color:var(--ink)}
  .tile-gold{background:var(--tile-gold)}
  .tile-lime{background:var(--tile-lime)}
  .tile-orange{background:var(--tile-orange)}
  .tile-label{font-family:"Patrick Hand",cursive;font-size:40px;line-height:1;height:46px}
  .tile-label.long{font-size:34px;text-align:center}
  .tile-icon{margin-top:22px;width:100px;height:100px}
  .tile-note{position:absolute;bottom:12px;font-family:"Noto Sans JP",sans-serif;font-weight:500;font-size:17px}
  .social-dots{margin-top:46px;display:flex;gap:10px}
  .social-dots span{width:46px;height:46px;border-radius:50%;background:var(--ink)}
</style>
</head>
<body>
<div class="canvas">

  <section class="rich-message">
    <div class="hero-photo" role="img" aria-label="口元に手を添えて微笑む女性の肌のアップ写真"></div>
    <div class="brand"><span class="brand-mark"></span>素肌研究室</div>
    <div class="tagline">
      <span>完全個室の特別空間を提供する</span>
      <span>プライベートエステサロン</span>
    </div>
    <div class="room-photo" role="img" aria-label="施術ベッドが並ぶ落ち着いた個室の写真"></div>
    <div class="care-photo" role="img" aria-label="フェイシャルトリートメントを受ける女性の写真"></div>
  </section>

  <nav class="rich-menu">
    <div class="menu-tile tile-gold">
      <div class="tile-label">HP</div>
      <svg class="tile-icon" viewBox="0 0 100 100" aria-hidden="true">
        <rect x="8" y="14" width="84" height="56" rx="4" fill="var(--ink)"/>
        <rect x="16" y="22" width="68" height="40" fill="var(--tile-gold)"/>
        <rect x="44" y="70" width="12" height="12" fill="var(--ink)"/>
        <rect x="30" y="82" width="40" height="6" rx="2" fill="var(--ink)"/>
      </svg>
    </div>
    <div class="menu-tile tile-lime">
      <div class="tile-label">Menu</div>
      <svg class="tile-icon" viewBox="0 0 100 100" aria-hidden="true">
        <rect x="8" y="8" width="84" height="84" rx="4" fill="var(--ink)"/>
        <g fill="var(--tile-lime)">
          <rect x="22" y="27" width="9" height="7"/><rect x="38" y="27" width="40" height="7"/>
          <rect x="22" y="46" width="9" height="7"/><rect x="38" y="46" width="40" height="7"/>
          <rect x="22" y="65" width="9" height="7"/><rect x="38" y="65" width="40" height="7"/>
        </g>
      </svg>
    </div>
    <div class="menu-tile tile-gold">
      <div class="tile-label">SNS</div>
      <div class="social-dots" aria-hidden="true"><span></span><span></span><span></span></div>
    </div>
    <div class="menu-tile tile-lime">
      <div class="tile-label long">Customers'<br>Opinions</div>
      <svg class="tile-icon" viewBox="0 0 100 100" style="margin-top:4px;width:90px;height:90px" aria-hidden="true">
        <ellipse cx="40" cy="40" rx="32" ry="24" fill="var(--ink)"/>
        <path d="M22 56 L14 74 L36 62 Z" fill="var(--ink)"/>
        <ellipse cx="64" cy="60" rx="28" ry="20" fill="var(--ink)" stroke="var(--tile-lime)" stroke-width="4"/>
        <path d="M78 74 L88 88 L70 78 Z" fill="var(--ink)"/>
      </svg>
      <div class="tile-note">お客さまの声</div>
    </div>
    <div class="menu-tile tile-orange">
      <div class="tile-label">Staff・Store</div>
      <svg class="tile-icon" viewBox="0 0 100 100" aria-hidden="true">
        <path d="M14 14 H86 L92 38 H8 Z" fill="var(--ink)"/>
        <path d="M8 38 H92 V46 Q83 54 74 46 Q65 54 56 46 Q47 54 38 46 Q29 54 20 46 Q14 52 8 46 Z" fill="var(--ink)"/>
        <rect x="16" y="52" width="68" height="36" fill="none" stroke="var(--ink)" stroke-width="6"/>
        <rect x="26" y="62" width="20" height="26" fill="var(--ink)"/>
        <rect x="54" y="62" width="20" height="14" fill="var(--ink)"/>
      </svg>
    </div>
    <div class="menu-tile tile-lime">
      <div class="tile-label">Reserve</div>
      <svg class="tile-icon" viewBox="0 0 100 100" aria-hidden="true">
        <rect x="10" y="16" width="80" height="74" rx="6" fill="var(--ink)"/>
        <rect x="26" y="8" width="8" height="16" rx="3" fill="var(--ink)"/>
        <rect x="66" y="8" width="8" height="16" rx="3" fill="var(--ink)"/>
        <g fill="var(--tile-lime)">
          <rect x="20" y="36" width="12" height="10"/><rect x="38" y="36" width="12" height="10"/><rect x="56" y="36" width="12" height="10"/><rect x="74" y="36" width="8" height="10"/>
          <rect x="20" y="52" width="12" height="10"/><rect x="38" y="52" width="12" height="10"/><rect x="56" y="52" width="12" height="10"/><rect x="74" y="52" width="8" height="10"/>
          <rect x="20" y="68" width="12" height="10"/><rect x="38" y="68" width="12" height="10"/><rect x="56" y="68" width="12" height="10"/>
        </g>
      </svg>
    </div>
  </nav>

</div>
</body>
</html>
```